Company or website name
- spinthebluereel.net
- Links to the website
- I am a DJ, this site will be used strictly a place where I will post new mixes I have done, sort of like a running blog and you will be able to listen to the most recent mix I posted or download, you will see artwork for the mix along with tracklist
- Other Facts

```html
<!DOCTYPE html>
<html lang="en">
<head>
<meta charset="utf-8">
<title>Spin The Blue Reel</title>
<link href="https://fonts.googleapis.com/css2?family=Arimo:wght@400;700&family=Libre+Baskerville:wght@700&display=swap" rel="stylesheet">
<style>
:root{
  --bg:#040506;
  --panel:#0a1c26;
  --panel-hi:#123748;
  --edge:#1f5f7e;
  --accent:#3a9ccc;
  --accent-soft:#6cb8dc;
  --gold:#e6bf3f;
  --text:#e8eef2;
  --muted:#8a9aa4;
  --thumb:#2a4a5c;
  --thumb-edge:#b8a47a;
}
*{margin:0;padding:0;box-sizing:border-box}
a{color:inherit;text-decoration:none}
html,body{width:720px;height:1200px;overflow:hidden;background:var(--bg);font-family:"Arimo",Arial,sans-serif;color:var(--text)}
.canvas{position:relative;width:720px;height:1200px;background:radial-gradient(ellipse at 50% 0%,#0c1a22 0%,var(--bg) 55%)}
.abs{position:absolute}

/* header */
.logo{left:62px;top:16px;font-family:"Libre Baskerville",Georgia,serif;font-weight:700;font-size:25px;color:#fff;letter-spacing:.3px}
.account{right:58px;top:10px;display:flex;gap:10px}
.account a{display:block;width:88px;height:22px;line-height:22px;text-align:center;font-size:10px;font-weight:700;color:#222;border-radius:3px;background:linear-gradient(#f2f2f2,#a9a9a9)}
.main-nav{right:58px;top:50px;display:flex;align-items:center}
.main-nav a{font-size:9px;color:#c9d3d9;padding:0 10px;border-left:1px solid #33444e}
.main-nav a:first-child{border-left:0}
.main-nav .current{font-size:12px;font-weight:700;color:#fff;padding:8px 18px;background:radial-gradient(ellipse at 50% 60%,#1f6d96 0%,rgba(4,5,6,0) 75%)}

/* hero */
.hero{left:62px;top:76px;width:600px;height:232px;border:1px solid #1b3846;overflow:hidden}
.hero-art{position:absolute;inset:0;background:radial-gradient(ellipse at 50% 35%,#dfe8ee 0%,#7fa6bb 22%,#1f4a60 48%,#070b0e 78%),#000}
.hero-arrow{position:absolute;top:100px;width:18px;height:28px}
.hero-arrow.prev{left:8px}.hero-arrow.next{right:8px}
.artist-bar{position:absolute;left:0;right:0;bottom:0;height:44px;background:linear-gradient(rgba(0,0,0,.2),rgba(0,0,0,.85));display:flex;justify-content:center;align-items:center;gap:22px}
.artist-bar a{font-size:8px;font-weight:700;color:var(--gold);letter-spacing:.3px}
.slider{left:62px;top:314px;width:658px;height:10px}

/* section titles */
.section-title{left:62px;width:600px;display:flex;align-items:center;gap:10px;font-size:12px;letter-spacing:2px;color:var(--accent-soft)}
.section-title::after{content:"";flex:1;height:1px;background:linear-gradient(90deg,var(--edge),rgba(31,95,126,0))}
.rss{display:inline-block;width:16px;height:10px;background:#e0a020;border-radius:2px}

.panel{left:62px;width:600px;border:1px solid var(--edge);background:linear-gradient(180deg,var(--panel-hi) 0%,var(--panel) 40%,#06121a 100%);box-shadow:0 0 10px rgba(58,156,204,.25)}

/* special features */
.special{top:352px;height:262px}
.feature-photo{left:10px;top:10px;width:270px;height:210px;background:linear-gradient(135deg,#5a5a5a 0%,#2e2e2e 45%,#8a8a8a 70%,#1c1c1c 100%)}
.feature-caption{left:16px;top:176px;width:260px}
.feature-caption .tag{font-size:9px;color:var(--gold);font-weight:700}
.feature-caption .line{font-size:10px;font-weight:700;color:#fff}
.feature-text{left:288px;top:14px;width:100px;font-size:7.5px;line-height:10.5px;color:#bfcbd2}
.more-info{left:335px;top:206px;font-size:7px}
.pager{left:10px;top:226px;width:378px;height:20px;display:flex;align-items:center;gap:3px;background:#071a24;padding:0 4px}
.pager span{display:block;min-width:17px;height:14px;line-height:14px;text-align:center;font-size:7px;color:#9fc6da;background:#10384c}
.pager .nav{background:var(--gold);color:#111;font-weight:700;padding:0 5px}
.pager .next{margin-left:auto}
.featured-artist{left:394px;top:10px;width:196px;height:238px;border:1px solid var(--edge);background:#081923}
.featured-artist h3{height:20px;line-height:20px;padding-left:8px;font-size:9px;color:var(--gold);background:linear-gradient(#1a4d66,#0d2c3b);letter-spacing:.5px}
.lead{display:flex;gap:8px;padding:8px}
.thumb{background:var(--thumb);border:2px solid var(--thumb-edge)}
.lead .thumb{width:40px;height:40px;flex:none}
.meta{font-size:7.5px;line-height:10px}
.meta .name{color:var(--accent-soft);font-weight:700}
.meta .name::before{content:"▸ ";color:var(--accent)}
.meta .stats{color:var(--muted)}
.meta .stats b{color:var(--accent-soft);font-weight:400;text-decoration:underline}
.guest-grid{display:grid;grid-template-columns:repeat(4,38px);gap:6px 9px;padding:2px 10px}
.guest-grid figure .thumb{width:38px;height:34px}
.guest-grid figcaption{font-size:6px;color:var(--muted);text-align:center;margin-top:1px}
.view-more{font-size:7px;color:var(--accent-soft)}

/* now playing */
.now-playing{top:658px;height:164px}
.col-head{height:16px;line-height:16px;font-size:8.5px;font-weight:700;color:#cfe3ee;text-align:center;background:linear-gradient(#1c5674,#0c2a39);letter-spacing:1px}
.brand-new{left:10px;top:8px;width:230px}
.brand-new .photo{margin:8px auto 0;width:126px;height:70px;background:linear-gradient(160deg,#3a3a3a,#bdbdbd 55%,#4a4a4a)}
.brand-new .meta{margin:8px 0 0 12px}
.whats-hot{left:258px;top:8px;width:180px}
.hot-row{display:flex;gap:8px;margin-top:8px}
.hot-row .photo{width:58px;height:36px;flex:none;background:linear-gradient(160deg,#2c2c2c,#aaa 55%,#3a3a3a);border:1px solid #4d6b7a}
.channels{left:468px;top:8px;width:122px}
.channels .col-head{font-size:6.5px;background:none;color:var(--accent-soft);text-align:left}
.channels .photo{width:52px;height:32px;margin:8px 0 0 30px;background:linear-gradient(160deg,#2c2c2c,#aaa 55%,#3a3a3a);border:1px solid #4d6b7a}
.now-playing .view-more{right:10px;bottom:6px}

/* news */
.news{top:864px;height:226px;background:linear-gradient(180deg,#0b222e 0%,#050f15 100%)}
.news-col-title{font-size:7.5px;font-weight:700;color:var(--accent-soft);padding-bottom:3px;border-bottom:1px solid var(--edge);margin-bottom:8px}
.featured-news{left:10px;top:10px;width:230px}
.featured-news .item{display:flex;gap:8px}
.featured-news .item .thumb{width:60px;height:60px;flex:none;border-color:#4d6b7a}
.featured-news .title{font-size:8.5px;font-weight:700;line-height:10px}
.featured-news .body{font-size:7px;line-height:9.5px;color:#aebcc4;margin-top:4px}
.recent-news{left:256px;top:10px;width:178px}
.recent-news .item{display:flex;gap:8px;margin-bottom:12px}
.recent-news .item .thumb{width:34px;height:34px;flex:none;border-color:#4d6b7a}
.past-news{left:450px;top:10px;width:140px}
.past-news p{font-size:7px;line-height:9.5px;color:#cdd7dc;margin-bottom:12px;width:90px}
.news .view-more{right:10px;bottom:6px}

/* footer */
.footer{left:62px;top:1116px;width:600px;text-align:center}
.footer nav{font-size:7px;color:#c3ccd1;display:flex;justify-content:center;gap:22px}
.footer .copy{font-size:6.5px;color:var(--muted);margin-top:4px}
.social{display:flex;justify-content:center;gap:6px;margin-top:8px}
.social span{width:13px;height:13px;border-radius:2px;background:#3c6fae}
.social span:nth-child(2){background:#2e7bb6}
.social span:nth-child(3){background:#4fb6e8}
</style>
</head>
<body>
<div class="canvas">

  <header>
    <div class="abs logo">Spin The Blue Reel</div>
    <div class="abs account"><a href="#">JOIN NOW</a><a href="#">LOGIN</a></div>
    <nav class="abs main-nav">
      <a class="current" href="#">HOME</a>
      <a href="#">OTHER MENU</a><a href="#">OTHER MENU</a><a href="#">OTHER MENU</a><a href="#">OTHER MENU</a>
    </nav>
  </header>

  <section class="abs hero">
    <div class="hero-art" role="img" aria-label="DJ turntable above a silhouetted crowd with raised hands under blue stage lights"></div>
    <svg class="hero-arrow prev" viewBox="0 0 18 28"><path d="M14 2 L4 14 L14 26" fill="none" stroke="#cfe3ee" stroke-width="3"/></svg>
    <svg class="hero-arrow next" viewBox="0 0 18 28"><path d="M4 2 L14 14 L4 26" fill="none" stroke="#cfe3ee" stroke-width="3"/></svg>
    <nav class="artist-bar">
      <a href="#">ORIN VALE</a><a href="#">KASH MERIDIAN</a><a href="#">THE LOWTIDE</a><a href="#">DEX MARLOWE</a><a href="#">B.Q.</a><a href="#">LIL TORVO</a><a href="#">SAGE ABERNATHY</a>
    </nav>
  </section>
  <svg class="abs slider" viewBox="0 0 658 10">
    <rect x="0" y="2" width="600" height="6" fill="#0d2735"/>
    <line x1="0" y1="5" x2="658" y2="5" stroke="#3a5868" stroke-width="1"/>
    <rect x="268" y="0" width="40" height="10" fill="#7fb9d6"/>
  </svg>

  <h2 class="abs section-title" style="top:330px">SPECIAL FEATURES</h2>
  <section class="abs panel special">
    <div class="abs feature-photo" role="img" aria-label="Two artists posing together in a studio portrait"></div>
    <div class="abs feature-caption">
      <div class="tag">Printing, Industry !</div>
      <div class="line">"Lorem Ipsum" Is Simply Dummy Text Of The Printing Industry !</div>
    </div>
    <p class="abs feature-text">Lorem Ipsum is simply dummy text of the printing and typesetting industry. Lorem Ipsum has been the standard dummy text ever since the 1500s, when an unknown printer took a galley of type and scrambled it to make a type specimen book. It has survived not only five centuries, but also the leap into electronic typesetting, remaining essentially unchanged. It was popularised in the 1960s with the release of sheets.</p>
    <a class="abs more-info view-more" href="#">more info</a>
    <div class="abs pager">
      <span class="nav">« PREV</span>
      <span>1</span><span>2</span><span>3</span><span>4</span><span>5</span><span>6</span><span>7</span><span>8</span><span>9</span><span>10</span><span>11</span><span>12</span><span>13</span>
      <span class="nav next">NEXT »</span>
    </div>
    <aside class="abs featured-artist">
      <h3>FEATURED ARTIST</h3>
      <div class="lead">
        <div class="thumb" role="img" aria-label="Featured artist portrait"></div>
        <div class="meta">
          <div class="name">DEX MARLOWE</div>
          <div>Lorem Ipsum" is</div>
          <div class="stats">Views: 1024 &nbsp;<b>Comments : 98</b></div>
        </div>
      </div>
      <div class="guest-grid">
        <figure><div class="thumb"></div><figcaption>Guest</figcaption></figure>
        <figure><div class="thumb"></div><figcaption>Guest</figcaption></figure>
        <figure><div class="thumb"></div><figcaption>Guest</figcaption></figure>
        <figure><div class="thumb"></div><figcaption>Guest</figcaption></figure>
        <figure><div class="thumb"></div><figcaption>Guest</figcaption></figure>
        <figure><div class="thumb"></div><figcaption>Guest</figcaption></figure>
        <figure><div class="thumb"></div><figcaption>Guest</figcaption></figure>
        <figure><div class="thumb"></div><figcaption>Guest</figcaption></figure>
        <figure><div class="thumb"></div><figcaption>Guest</figcaption></figure>
        <figure><div class="thumb"></div><figcaption>Guest</figcaption></figure>
        <figure><div class="thumb"></div><figcaption>Guest</figcaption></figure>
        <figure><div class="thumb"></div><figcaption>Guest</figcaption></figure>
      </div>
      <div class="view-more" style="text-align:right;padding-right:8px">View More</div>
    </aside>
  </section>

  <h2 class="abs section-title" style="top:636px">NOW PLAYING</h2>
  <section class="abs panel now-playing">
    <div class="abs brand-new">
      <div class="col-head">BRAND NEW</div>
      <div class="photo" role="img" aria-label="Artist standing in a black graphic t-shirt"></div>
      <div class="meta">
        <div class="name">DEX MARLOWE</div>
        <div style="font-weight:700">"Lorem Ipsum" Is Simply Dummy y !</div>
        <div class="stats">Views: 1024 &nbsp;<b>Comments : 98</b></div>
      </div>
    </div>
    <div class="abs whats-hot">
      <div class="col-head">WHAT'S HOT</div>
      <div class="hot-row"><div class="photo" role="img" aria-label="Mix artwork"></div><div class="meta"><div class="name">DEX MARLOWE</div><div>Lorem Ipsum" is</div><div class="stats">Views: 1024 <b>Comments : 98</b></div></div></div>
      <div class="hot-row"><div class="photo" role="img" aria-label="Mix artwork"></div><div class="meta"><div class="name">DEX MARLOWE</div><div>Lorem Ipsum" is</div><div class="stats">Views: 1024 <b>Comments : 98</b></div></div></div>
      <div class="hot-row"><div class="photo" role="img" aria-label="Mix artwork"></div><div class="meta"><div class="name">DEX MARLOWE</div><div>Lorem Ipsum" is</div><div class="stats">Views: 1024 <b>Comments : 98</b></div></div></div>
    </div>
    <div class="abs channels">
      <div class="col-head">FEATURED CHANNELS</div>
      <div class="photo" role="img" aria-label="Channel artwork"></div>
      <div class="photo" role="img" aria-label="Channel artwork"></div>
      <div class="photo" role="img" aria-label="Channel artwork"></div>
    </div>
    <a class="abs view-more" href="#">View More</a>
  </section>

  <h2 class="abs section-title" style="top:842px">NEWS &amp; UPDATES <span class="rss"></span></h2>
  <section class="abs panel news">
    <div class="abs featured-news">
      <div class="news-col-title">FEATURES NEWS</div>
      <div class="item">
        <div class="thumb" role="img" aria-label="News story image"></div>
        <div>
          <div class="title">Lorem Ipsum is simply dummy text of the printing and typesetting industry</div>
          <p class="body">Lorem Ipsum is simply dummy text of the printing and typesetting industry. Lorem Ipsum has been the industry's standard dummy text ever since the 1500s, when an unknown printer took a galley of type and scrambled it to make a type specimen book. It has survived not only five centuries, but also.</p>
        </div>
      </div>
    </div>
    <div class="abs recent-news">
      <div class="news-col-title">RECENT &nbsp; NEWS</div>
      <div class="item"><div class="thumb" role="img" aria-label="News image"></div><div class="meta"><div class="name">DEX MARLOWE</div><div>Lorem Ipsum" is</div><div class="stats">Views: 1024 <b>Comments : 98</b></div></div></div>
      <div class="item"><div class="thumb" role="img" aria-label="News image"></div><div class="meta"><div class="name">DEX MARLOWE</div><div>Lorem Ipsum" is</div><div class="stats">Views: 1024 <b>Comments : 98</b></div></div></div>
      <div class="item"><div class="thumb" role="img" aria-label="News image"></div><div class="meta"><div class="name">DEX MARLOWE</div><div>Lorem Ipsum" is</div><div class="stats">Views: 1024 <b>Comments : 98</b></div></div></div>
    </div>
    <div class="abs past-news">
      <div class="news-col-title">PAST &nbsp; NEWS</div>
      <p>Lorem Ipsum is simply dummy text of the printing</p>
      <p>Lorem Ipsum is simply dummy text of the printing</p>
      <p>Lorem Ipsum is simply dummy text of the printing</p>
      <p>Lorem Ipsum is simply dummy text of the printing</p>
    </div>
    <a class="abs view-more" href="#">View More</a>
  </section>

  <footer class="abs footer">
    <nav><a>Privacy Policy</a><a>Terms of Use</a><a>About Us</a></nav>
    <p class="copy">© 2010 spinthebluereel.net. All rights reserved.</p>
    <div class="social"><span></span><span></span><span></span></div>
  </footer>

</div>
</body>
</html>
```